Brisko Sky Park needs a new upscale business card design for our high end aircraft hangar complex

Brisko Sky Park (BSP) is a large, upscale jet hangar complex in the US housing expensive aircraft. We need a new business card design, using our current logo. We will be attending a industry convention and need a card design that will stand out and be remembered by aircraft owners and private pilots.

Target Market(s)

Aircraft pilots or owners looking for a new upscale hangar

Industry/Entity Type

Airport

Contact Information for Business Card

I like to use very heavy card stock, 400#, double sided. Square, no rounded edges please.

Colors
3276b5
0255a3
85abd2

Requirements
Must have
• An expensive, classy design, vivid colors.
Nice to have
• Needs to look very expensive and classy, and have some "pop". Designer must be able to download or copy my current typeface or fonts.
• One card side might be black with the "Logo and Brisko Sky Park Double line image in blue (or try gold, or glossy black), and perhaps have a grayed out "K480 jet silhouette". The other card side would have our contact info, and perhaps the "BSP Logo only". I'd like my contact info 'stacked', not in a paragraph format.
Should not have
• Should not look "too busy". Having a double-sided card will help.

```html
<!DOCTYPE html>
<html lang="en">
<head>
<meta charset="utf-8">
<title>Brisko Sky Park — Business Card</title>
<link rel="stylesheet" href="https://fonts.googleapis.com/css2?family=Roboto:wght@400;500;700&display=swap">
<style>
  :root {
    --backdrop: #8e8f91;
    --card-black: #111213;
    --blue-deep: #0b2f5c;
    --blue-mid: #1d568f;
    --blue-brand: #2a64a6;
    --silver: #b9bcc0;
    --text-light: #eef2f7;
    --text-soft: #d4dbe4;
    --card-w: 750px;
    --card-h: 428px;
  }
  * { box-sizing: border-box; margin: 0; padding: 0; }
  html, body {
    width: 1105px; height: 1200px; overflow: hidden;
    background: var(--backdrop);
    font-family: "Roboto", Arial, sans-serif;
  }
  .card {
    position: absolute; left: 177px;
    width: var(--card-w); height: var(--card-h);
    background: var(--card-black);
    overflow: hidden;
  }
  .card--front { top: 140px; }
  .card--back { top: 655px; }

  .front-panel { position: absolute; inset: 0; width: 100%; height: 100%; }

  .brand {
    position: absolute;
    display: flex; align-items: center; gap: 14px;
    color: var(--blue-brand);
    font-weight: 700; text-transform: uppercase;
    letter-spacing: 1px; line-height: 1.05;
  }
  .brand__dot {
    width: 22px; height: 22px; border-radius: 50%;
    background: var(--blue-brand); flex: none;
  }
  .brand__name { font-size: 40px; }
  .card--front .brand { left: 62px; top: 95px; width: 320px; }
  .card--back .brand { left: 0; right: 0; top: 150px; justify-content: center; }

  .contact {
    position: absolute; right: 48px; top: 112px;
    text-align: right; color: var(--text-soft);
  }
  .contact__name { font-size: 25px; font-weight: 500; color: var(--text-light); }
  .contact__title { font-size: 19px; margin-top: 3px; color: var(--text-light); }
  .contact__address { font-size: 18px; line-height: 27px; margin-top: 24px; margin-right: 0; }
  .contact__lines { list-style: none; margin-top: 16px; }
  .contact__line {
    display: flex; justify-content: flex-end; align-items: center; gap: 10px;
    font-size: 18px; height: 29px;
  }
  .contact__icon { width: 18px; height: 18px; fill: var(--text-light); flex: none; }

  .back-url {
    position: absolute; left: 0; right: 0; top: 358px;
    text-align: center; font-size: 17px; letter-spacing: 3.5px;
    color: var(--text-soft);
  }
</style>
</head>
<body>

<section class="card card--front">
  <svg class="front-panel" viewBox="0 0 750 428" preserveAspectRatio="none" aria-hidden="true">
    <defs>
      <radialGradient id="panelGlow" cx="62%" cy="45%" r="70%">
        <stop offset="0" stop-color="#285f98"/>
        <stop offset="1" stop-color="#0a2c57"/>
      </radialGradient>
    </defs>
    <polygon points="460,0 750,0 750,428 332,428" fill="url(#panelGlow)"/>
    <polygon points="452,0 459,0 331,428 324,428" fill="#b9bcc0"/>
  </svg>

  <div class="brand">
    <span class="brand__dot"></span>
    <span class="brand__name">Brisko<br>Sky Park</span>
  </div>

  <div class="contact">
    <p class="contact__name">Evan Harlow</p>
    <p class="contact__title">President</p>
    <p class="contact__address">4120 Larkspur Lane<br>Cedar Bluff, NY 12045</p>
    <ul class="contact__lines">
      <li class="contact__line">555 214 7390
        <svg class="contact__icon" viewBox="0 0 20 20"><path d="M2 7c0-3 3-4 8-4s8 1 8 4v2h-4V7.5c-1-.6-7-.6-8 0V9H2z"/><path d="M5 10l2-3h6l2 3 1 6H4z"/></svg>
      </li>
      <li class="contact__line">555 368 1427
        <svg class="contact__icon" viewBox="0 0 20 20"><path d="M6 1h8a1 1 0 0 1 1 1v16a1 1 0 0 1-1 1H6a1 1 0 0 1-1-1V2a1 1 0 0 1 1-1zm1 3v10h6V4zm3 11.5a1 1 0 1 0 0 2 1 1 0 0 0 0-2z"/></svg>
      </li>
      <li class="contact__line">555 902 6613
        <svg class="contact__icon" viewBox="0 0 20 20"><path d="M5 2h10v5H5z"/><path d="M2 8h16v7H2zm3 5h10v5H5z"/></svg>
      </li>
      <li class="contact__line">evan@briskosky.com
        <svg class="contact__icon" viewBox="0 0 20 20"><path d="M2 5h16v1l-8 5-8-5z"/><path d="M2 8l8 5 8-5v7H2z"/></svg>
      </li>
      <li class="contact__line">www.briskosky.com
        <svg class="contact__icon" viewBox="0 0 20 20"><circle cx="10" cy="10" r="8"/><path d="M6 6l4 1 1 3-3 1-1 3-2-3zM12 12l3-1-1 4z" fill="#1d568f"/></svg>
      </li>
    </ul>
  </div>
</section>

<section class="card card--back">
  <div class="brand">
    <span class="brand__dot"></span>
    <span class="brand__name">Brisko<br>Sky Park</span>
  </div>
  <p class="back-url">www.briskosky.com</p>
</section>

</body>
</html>
```